Buchcover-Design für Ratgeber
Zielgruppe
Wir veröffentlichen Ebooks und Taschenbücher auf Lumora und benötigen für ein aktuelles Projekt noch ein Ebook Cover. Die Zielgruppe sind werdende und frisch gebackene Väter im Alter zwischen 25 und 40 Jahren.
Titel: KNIRPSOLOGIE, Vati kriegt das hin
Untertitel: Raus aus der Panik und rein ins Vater werden mit Verantwortung, Herz und Stil
Autor: Gernot Wallbrecht
Der Fokus des Buches richtet sich darauf, Vätern und denen, die es noch werden wollen, wertvolle Tipps und Handlungsempfehlungen mitzugeben, wie man sich als moderner, engagiertet Vater positioniert. Es richtet sich an Männer, die sich aktiv in die Erziehung ihres Kindes einbringen wollen und mehr sein wollen, als nur der Ernährer und Geldverdiener. Diese Zielgruppe ist bereit, Zeit zu investieren und sich darum zu bemühen, sich das Wissen anzueignen, wie sie ihre Partnerin während Schwangerschaft und Geburt unterstützen und wie sie eine starke Vater-Kind-Beziehung aufbauen können.
Das Hauptproblem dieser Zielgruppe ist, dass sie nur wenig Ahnung von Kindererziehung oder Schwangerschaft hat. Daher herrscht hier eine große Ratlosigkeit und Unsicherheit vor, da sie zum einen möglichst alles richtig machen will, zum Anderen aber nicht weiß, wie sie das anstellen und worauf alles zu achten ist.
Das Buch soll mit Cover und Titel die Botschaft senden, dass diese Sorgen unnötig sind und dass Daddy schon alles regelt. natürlich nur, wenn er das Buch gelesen hat ;-)
Aufgabenstellung
Wir hätten gerne ein Cover, welches ein kreatives Konzept abbildet und nicht nach Quobix-Standard bloß Titel, Stockfoto und den Namen des Autors darstellt. Ich denke es eignet sich hier mit dem Titel etwas auszuprobieren, da so ein Wortspiel wahrscheinlich einiges an kreativen Möglichkeiten bietet. Grundsätzlich sollten Cover, Titel und Untertitel miteinander harmonieren und ein schlüssiges Konzept darstellen, welches die Botschaft des Buches einfach rüber bringt.
Ansonsten haben wir keine weiteren Angaben wie Farben, Beispielcover usw. Hier könnt ihr kreativ werden!

```html
<!DOCTYPE html>
<html lang="de">
<head>
<meta charset="utf-8">
<title>Knirpsologie – Buchcover</title>
<link rel="stylesheet" href="https://fonts.googleapis.com/css2?family=Courier+Prime:wght@400;700&family=Quicksand:wght@400;500&display=swap">
<style>
  :root {
    --page: #ffffff;
    --cover-grey: #a6a7ab;
    --cover-grey-light: #b3b4b8;
    --quote-grey: #c6c7cb;
    --title-orange: #d35f0a;
    --title-ink: #2a2838;
    --subtitle-white: #ffffff;
    --body-ink: #2e2e33;
    --photo-shadow: #7d8596;
    --photo-skin: #c9a58c;
    --photo-light: #e6e4e4;
  }
  * { margin: 0; padding: 0; box-sizing: border-box; }
  html, body {
    width: 750px; height: 1200px; overflow: hidden;
    background: var(--page);
  }
  .canvas { position: relative; width: 750px; height: 1200px; }
  .book-cover {
    position: absolute; left: 75px; top: 120px;
    width: 600px; height: 960px; overflow: hidden;
    background: linear-gradient(180deg, var(--cover-grey) 0%, var(--cover-grey-light) 55%, var(--cover-grey) 100%);
    box-shadow: 4px 5px 8px rgba(0,0,0,0.25);
  }
  .cover-photo {
    position: absolute; left: 0; right: 0; top: 420px; bottom: 0;
    background:
      radial-gradient(ellipse 45% 40% at 78% 38%, var(--photo-skin) 0%, rgba(201,165,140,0) 100%),
      radial-gradient(ellipse 35% 30% at 45% 30%, rgba(220,190,170,0.9) 0%, rgba(220,190,170,0) 100%),
      radial-gradient(ellipse 60% 35% at 55% 85%, var(--photo-light) 0%, rgba(230,228,228,0) 100%),
      linear-gradient(180deg, rgba(166,167,171,0) 0%, var(--photo-shadow) 70%, #8d93a0 100%);
  }
  .quote-mark {
    position: absolute;
    font-family: "Courier Prime", Georgia, serif; font-weight: 700;
    color: var(--quote-grey); line-height: 1;
  }
  .quote-mark--top { left: 455px; top: -8px; font-size: 230px; }
  .quote-mark--mid { left: 5px; top: 188px; font-size: 230px; }
  .author {
    position: absolute; left: 38px; top: 34px;
    font-family: "Quicksand", sans-serif; font-weight: 400;
    font-size: 18px; color: var(--body-ink);
  }
  .book-title {
    position: absolute; left: 36px; top: 150px;
    font-family: "Courier Prime", monospace; font-weight: 700;
    font-size: 72px; line-height: 1; letter-spacing: -1px;
    color: var(--title-ink); white-space: nowrap;
  }
  .book-title__accent { color: var(--title-orange); font-size: 86px; }
  .book-tagline {
    position: absolute; right: 38px; top: 250px; text-align: right;
    font-family: "Courier Prime", monospace; font-weight: 700;
    font-size: 52px; line-height: 58px; color: var(--subtitle-white);
    text-transform: uppercase;
  }
  .book-subtitle {
    position: absolute; left: 38px; top: 368px; width: 210px;
    font-family: "Quicksand", sans-serif; font-weight: 400;
    font-size: 20px; line-height: 26px; color: var(--body-ink);
  }
</style>
</head>
<body>
<div class="canvas">
  <div class="book-cover">
    <div class="cover-photo" role="img" aria-label="Foto: lachender Vater hält sein Baby hoch, Stirn an Stirn"></div>
    <span class="quote-mark quote-mark--top" aria-hidden="true">”</span>
    <span class="quote-mark quote-mark--mid" aria-hidden="true">”</span>
    <p class="author">Gernot Wallbrecht</p>
    <h1 class="book-title"><span class="book-title__accent">KNIRPS</span>ologie</h1>
    <p class="book-tagline">Vati kriegt<br>das hin</p>
    <p class="book-subtitle">Raus aus der Panik und rein ins Vater werden mit Verantwortung, Herz und Stil</p>
  </div>
</div>
</body>
</html>
```